Business Card Design Project

We are rebranding an existing automotive collision repair business. The business is called dentworks garage. I have attached logo but I'm not tied to that. I want to leave this wide open.

I want this card to say we are professional, competent, cutting edge. We are focused on customers and use a lot of the latest technology to make the customer experience different. We sign customers in on iPads. Paperwork I signed electronically and updates are sent via text, email, logging on a website or as they wish. I want this innovation and image to come through in our cards

Target Market(s)

60%. Women 40% men. Age 35-60

Industry/Entity Type

Automotive

Requirements
Must have
• The card must have name, title, phone,email, cell, web page

```html
<!DOCTYPE html>
<html lang="en">
<head>
<meta charset="utf-8">
<title>Dentworks Garage – Business Card</title>
<link href="https://fonts.googleapis.com/css2?family=Montserrat:wght@300;400;600;800&display=swap" rel="stylesheet">
<style>
  :root {
    --bg: #eef3f4;
    --card-white: #ffffff;
    --card-dark: #4a4a4a;
    --card-dark-deep: #363636;
    --slate: #525252;
    --teal: #36a3a6;
    --orange: #f5891f;
    --green: #7ac143;
    --ink: #3a3a3a;
    --line: #8a8a8a;
  }
  * { box-sizing: border-box; margin: 0; padding: 0; }
  html, body { width: 1200px; height: 1000px; overflow: hidden; }
  body {
    background: var(--bg);
    font-family: "Montserrat", sans-serif;
    position: relative;
  }

  .card {
    position: absolute;
    overflow: hidden;
    box-shadow: 0 6px 22px rgba(0,0,0,.12);
  }
  .card svg.decor { position: absolute; inset: 0; }

  /* ---------- front (portrait) ---------- */
  .card-front {
    left: 110px; top: 168px;
    width: 380px; height: 665px;
    background: var(--card-white);
  }
  .front-brand {
    position: absolute; left: 96px; top: 60px;
    display: flex; align-items: center; gap: 8px;
    font-weight: 800; font-size: 19px; color: var(--green);
    letter-spacing: .2px;
  }
  .front-brand .dot {
    width: 12px; height: 12px; border-radius: 50%; background: var(--green);
  }
  .holder {
    position: absolute; right: 40px; top: 138px; text-align: right;
  }
  .holder-name {
    font-weight: 400; font-size: 19px; color: var(--orange); letter-spacing: .6px;
  }
  .holder-name strong { font-weight: 600; }
  .holder-title {
    font-weight: 400; font-size: 14px; color: var(--ink); letter-spacing: 1px; margin-top: 2px;
  }
  .contact-list { list-style: none; }
  .contact-row {
    position: absolute; height: 18px;
    display: flex; align-items: center; gap: 6px;
    white-space: nowrap;
  }
  .contact-label {
    background: var(--slate); color: #fff;
    font-weight: 600; font-size: 10px; letter-spacing: .5px;
    padding: 2px 4px 1px;
  }
  .contact-value {
    color: var(--orange); font-weight: 300; font-size: 12px; letter-spacing: .3px;
  }

  /* ---------- back (landscape) ---------- */
  .card-back {
    left: 560px; top: 330px;
    width: 580px; height: 332px;
    background: linear-gradient(160deg, var(--card-dark) 0%, var(--card-dark-deep) 100%);
  }
  .back-brand {
    position: absolute; left: 0; right: 0; top: 128px;
    display: flex; justify-content: center; align-items: center; gap: 12px;
    font-weight: 800; font-size: 38px; color: var(--green); letter-spacing: .5px;
  }
  .back-brand .dot {
    width: 18px; height: 18px; border-radius: 50%; background: var(--green);
  }
  .back-web {
    position: absolute; left: 0; right: 0; top: 190px; text-align: center;
    color: #f2f2f2; font-weight: 400; font-size: 13px; letter-spacing: 1.2px;
  }
</style>
</head>
<body>

  <!-- Front of card -->
  <section class="card card-front" aria-label="Business card front">
    <svg class="decor" width="380" height="665" viewBox="0 0 380 665" aria-hidden="true">
      <defs>
        <linearGradient id="footGrad" x1="0" y1="0" x2="1" y2="1">
          <stop offset="0" stop-color="#7aaeb5"/>
          <stop offset="1" stop-color="#5a8f98"/>
        </linearGradient>
      </defs>
      <!-- teal accent band -->
      <polygon points="0,118 210,100 210,110 0,128" fill="var(--teal)"/>
      <!-- dark triangle -->
      <polygon points="380,205 380,290 285,290" fill="var(--slate)"/>
      <!-- connector lines -->
      <g fill="none" stroke="var(--line)" stroke-width="1">
        <polyline points="0,282 160,282 178,309"/>
        <polyline points="0,300 145,300 158,335"/>
        <polyline points="0,330 40,330 58,361"/>
        <polyline points="0,348 100,348 118,389"/>
      </g>
      <g fill="var(--orange)">
        <circle cx="178" cy="309" r="7"/>
        <circle cx="158" cy="335" r="7"/>
        <circle cx="58" cy="361" r="7"/>
        <circle cx="118" cy="389" r="7"/>
      </g>
      <!-- footer block -->
      <polygon points="175,540 380,505 380,665 150,665" fill="url(#footGrad)"/>
    </svg>

    <div class="front-brand"><span class="dot"></span>dentworks garage</div>

    <div class="holder">
      <p class="holder-name">YOUR <strong>NAME HERE</strong></p>
      <p class="holder-title">TITLE</p>
    </div>

    <ul class="contact-list">
      <li class="contact-row" style="left:190px;top:300px"><span class="contact-label">PH:</span><span class="contact-value">000 0000 000</span></li>
      <li class="contact-row" style="left:170px;top:326px"><span class="contact-label">CELL:</span><span class="contact-value">000 0000 000</span></li>
      <li class="contact-row" style="left:70px;top:352px"><span class="contact-label">EMAIL:</span><span class="contact-value">INFO@DENTWORKSGARAGE.COM</span></li>
      <li class="contact-row" style="left:130px;top:380px"><span class="contact-label">WEB:</span><span class="contact-value">DENTWORKSGARAGE.COM</span></li>
    </ul>
  </section>

  <!-- Back of card -->
  <section class="card card-back" aria-label="Business card back">
    <div class="back-brand"><span class="dot"></span>dentworks garage</div>
    <p class="back-web">DENTWORKSGARAGE.COM</p>
  </section>

</body>
</html>
```